Design some Business Cards

Note: Designs submitted so far are too heavy. Too much bright red color. I would like to restate that I want a white business card with minimal use of red/green or any other color.

I want to create a business card for a financial advisory. Name of the company is "TelvaQuin Wealth Partners". The company advises clients on investments in global equity and real estate markets.

I want a CLEAN and MINIMALIST design. I want a white business card with a tinge of red. Don't want a coloured card.

An example of front side of the business card I have with me. Please see attached file BC1. I also need a design for the back side of the business card.
These are only examples. No need to mimic these. I am open to all designs.

Details I want on the business card as follows:

Name: Dinesh K. Varma

Designation: Advisor

Address: 612, Maple Ridge Co-operative Society,
Beside QuikBazar, Lake Road, Veltora, 400213.

Tel: (+91) 98271 53308

Website: [url removed, login to view]

Email: [url removed, login to view]@[url removed, login to view]

I want to add the following comparison of "What We Do" and "What We Don't Do" (i.e. what our competition does.)
So basically on the business card itself, I want these differences highlighted.

Here's the text:

What We Do | What We Don't Do
|
Prudent Advise | Salesy Pitches
Build Your Portfolio | Sell You Products
Focused, Principled Investing | Double-your-money-guaranteed
Comprehensive Planning | Short-term Trading

Please attached examples that I found for Dos and Don'ts. These are just examples. No need to mimic these. I am OPEN TO ALL IDEAS.

I am also attaching the logo files.

The style has to be highly professional, sophisticated and slick.
I would describe the requirement as below:

1. Trustworthy - People give us their savings to manage. Trust is essential.
2. Elegant / classy - This is a top investment management company.
3. Clean

```html
<!DOCTYPE html>
<html lang="en">
<head>
<meta charset="utf-8">
<title>TelvaQuin Wealth Partners — Business Cards</title>
<link rel="stylesheet" href="https://fonts.googleapis.com/css2?family=Montserrat:wght@400;600;700&family=Quicksand:wght@400;500;600&display=swap">
<style>
  :root {
    --bg: #e9eaec;
    --card: #ffffff;
    --ink: #2b2b2b;
    --muted: #6a6a6a;
    --red: #d4202a;
    --green: #1f8a3a;
    --shadow: 0 10px 28px rgba(0,0,0,0.18);
  }
  * { box-sizing: border-box; margin: 0; padding: 0; }
  html, body { width: 1200px; height: 900px; overflow: hidden; }
  body {
    background: var(--bg);
    font-family: "Quicksand", sans-serif;
    color: var(--ink);
    display: flex;
    align-items: center;
    justify-content: center;
    gap: 60px;
  }
  .card {
    width: 530px;
    height: 303px;
    background: var(--card);
    box-shadow: var(--shadow);
    position: relative;
  }
  .brand {
    display: flex;
    align-items: center;
    gap: 10px;
  }
  .brand-mark {
    width: 14px; height: 14px;
    background: var(--red);
  }
  .brand-name {
    font-family: "Montserrat", sans-serif;
    font-weight: 600;
    font-size: 19px;
    letter-spacing: 0.5px;
    color: var(--ink);
  }

  /* back: what we do / don't do */
  .card-back .brand {
    position: absolute;
    top: 46px; left: 0; right: 0;
    justify-content: center;
  }
  .compare {
    position: absolute;
    top: 108px; left: 30px; right: 30px;
    display: grid;
    grid-template-columns: 1fr 1fr;
    column-gap: 34px;
  }
  .compare-col h2 {
    font-family: "Montserrat", sans-serif;
    font-weight: 600;
    font-size: 15px;
    margin-bottom: 10px;
  }
  .compare-do { text-align: right; }
  .compare-do h2 { color: var(--green); }
  .compare-dont h2 { color: var(--red); }
  .compare-col ul { list-style: none; }
  .compare-col li {
    font-size: 13.5px;
    font-weight: 500;
    color: var(--muted);
    line-height: 1.65;
    white-space: nowrap;
  }
  .compare-do li::after { content: "\2022"; color: var(--ink); margin-left: 5px; }
  .compare-dont li::before { content: "\2022"; color: var(--ink); margin-right: 5px; }

  /* front: identity and contacts */
  .person {
    position: absolute;
    top: 50px; left: 40px;
  }
  .person-name {
    font-family: "Montserrat", sans-serif;
    font-weight: 700;
    font-size: 17px;
  }
  .person-role {
    font-size: 11px;
    color: var(--muted);
    margin-top: 2px;
  }
  .card-front .brand {
    position: absolute;
    top: 92px; right: 40px;
  }
  .contacts {
    position: absolute;
    left: 150px; right: 30px; bottom: 24px;
    list-style: none;
  }
  .contacts li {
    display: flex;
    align-items: flex-start;
    gap: 10px;
    font-size: 12.5px;
    font-weight: 500;
    line-height: 1.55;
    margin-top: 4px;
  }
  .contacts svg { width: 14px; height: 14px; flex: none; margin-top: 3px; }
</style>
</head>
<body>

  <section class="card card-back">
    <div class="brand">
      <span class="brand-mark"></span>
      <span class="brand-name">TelvaQuin Wealth Partners</span>
    </div>
    <div class="compare">
      <div class="compare-col compare-do">
        <h2>What We Do</h2>
        <ul>
          <li>Prudent Advise</li>
          <li>Build Your Portfolio</li>
          <li>Focused Principled Investing</li>
          <li>Comprehensive Planning</li>
        </ul>
      </div>
      <div class="compare-col compare-dont">
        <h2>What We Don't Do</h2>
        <ul>
          <li>Salesy Pitches</li>
          <li>Sell You Products</li>
          <li>Double-your-money-guaranteed</li>
          <li>Short-term Trading</li>
        </ul>
      </div>
    </div>
  </section>

  <section class="card card-front">
    <div class="person">
      <p class="person-name">Dinesh K. Varma</p>
      <p class="person-role">Advisor</p>
    </div>
    <div class="brand">
      <span class="brand-mark"></span>
      <span class="brand-name">TelvaQuin Wealth Partners</span>
    </div>
    <ul class="contacts">
      <li>
        <svg viewBox="0 0 24 24" aria-hidden="true"><path fill="#2b2b2b" d="M6.6 10.8a15.1 15.1 0 0 0 6.6 6.6l2.2-2.2a1 1 0 0 1 1-.25 11.4 11.4 0 0 0 3.6.57 1 1 0 0 1 1 1V20a1 1 0 0 1-1 1A17 17 0 0 1 3 4a1 1 0 0 1 1-1h3.5a1 1 0 0 1 1 1c0 1.25.2 2.45.57 3.57a1 1 0 0 1-.25 1z"/></svg>
        <span>(+91) 98271 53308</span>
      </li>
      <li>
        <svg viewBox="0 0 24 24" aria-hidden="true"><rect x="2.5" y="5" width="19" height="14" fill="none" stroke="#2b2b2b" stroke-width="2"/><path d="M3 6l9 7 9-7" fill="none" stroke="#2b2b2b" stroke-width="2"/></svg>
        <span>telvaquin.partners@postvale.com</span>
      </li>
      <li>
        <svg viewBox="0 0 24 24" aria-hidden="true"><g fill="none" stroke="#2b2b2b" stroke-width="1.8"><circle cx="12" cy="12" r="9"/><ellipse cx="12" cy="12" rx="4" ry="9"/><path d="M3 12h18M5 7h14M5 17h14"/></g></svg>
        <span>www.telvaquin.com</span>
      </li>
      <li>
        <svg viewBox="0 0 24 24" aria-hidden="true"><path fill="#2b2b2b" d="M12 2a7 7 0 0 0-7 7c0 5.2 7 13 7 13s7-7.8 7-13a7 7 0 0 0-7-7zm0 9.5A2.5 2.5 0 1 1 12 6.5a2.5 2.5 0 0 1 0 5z"/></svg>
        <span>612, Maple Ridge Co-operative Society,<br>Beside QuikBazar, Lake Road, Veltora, 400213.</span>
      </li>
    </ul>
  </section>

</body>
</html>
```